Harbor Wick Co Banner Ad for Upcoming holidays

We would like for you to design an ad for Memorial day and Father's Day. For Memorial Day the sale will be 25% OFF select candles and free shipping when you order $50 or more.
For father's day the deal will be get 30% off all candles and free shipping when you order $75 or more.
Please note: These banners will be on our website, they do not require our logo.Banner size: 314 height x 783 width

Industry/Entity Type

Shipping

Requirements
Must have
• Banner size: 314 height x 783 width
Nice to have
• Picture of our unforgettable candle
Should not have
• Logo

```html
<!DOCTYPE html>
<html lang="en">
<head>
<meta charset="utf-8">
<title>Harbor Wick Co — Memorial Day Sale</title>
<link rel="stylesheet" href="https://fonts.googleapis.com/css2?family=Anton&family=Kalam:wght@700&family=EB+Garamond:wght@600&display=swap">
<style>
  :root {
    --paper: #ffffff;
    --ink: #111111;
    --band: #000000;
    --band-text: #ffffff;
    --flag-red: #d52b2b;
    --flag-blue: #2c3f8f;
    --flag-white: #f4f4f4;
    --product-dark: #1a1a1a;
    --product-light: #ececec;
  }
  * { margin: 0; padding: 0; box-sizing: border-box; }
  html, body {
    width: 1200px; height: 481px; overflow: hidden; background: var(--paper);
  }
  .banner {
    position: relative; width: 1200px; height: 481px; background: var(--paper); overflow: hidden;
  }
  .flag-art {
    position: absolute; left: 0; top: 0; width: 1200px; height: 395px;
  }
  .product-photo {
    position: absolute; left: 835px; top: 78px; width: 310px; height: 317px;
  }
  .headline {
    position: absolute; left: 74px; top: 216px;
    font-family: "Anton", "Impact", sans-serif;
    font-weight: 400;
    font-size: 70px; line-height: 1; letter-spacing: 0;
    color: var(--ink);
    white-space: nowrap;
    transform: scaleX(1.3); transform-origin: left top;
    text-shadow: 2px 2px 0 var(--paper), -1px -1px 0 var(--paper);
  }
  .fine-print {
    position: absolute; left: 8px; top: 348px;
    font-family: "Kalam", cursive;
    font-weight: 700;
    font-size: 26px; line-height: 1; color: var(--ink);
    white-space: nowrap;
  }
  .offer-band {
    position: absolute; left: 0; top: 395px; width: 1200px; height: 86px;
    background: var(--band);
  }
  .offer-text {
    position: absolute; left: 181px; top: 50%;
    transform: translateY(-50%);
    font-family: "EB Garamond", "Times New Roman", serif;
    font-weight: 600; color: var(--band-text);
    font-size: 45px; line-height: 1; white-space: nowrap;
  }
  .offer-text .percent { font-size: 72px; }
</style>
</head>
<body>
<main class="banner">
  <svg class="flag-art" viewBox="0 0 1200 395" preserveAspectRatio="none" role="img" aria-label="Painted brush-stroke American flag in red, white and blue">
    <defs>
      <linearGradient id="flagWash" x1="0" y1="0" x2="1" y2="0.5">
        <stop offset="0" stop-color="var(--flag-blue)"/>
        <stop offset="0.3" stop-color="var(--flag-blue)"/>
        <stop offset="0.42" stop-color="var(--flag-red)"/>
        <stop offset="0.75" stop-color="var(--flag-red)"/>
        <stop offset="1" stop-color="var(--flag-white)"/>
      </linearGradient>
    </defs>
    <path d="M0 0 H1200 V90 C1020 130 900 190 800 230 C660 290 460 345 280 352 C170 356 70 320 0 300 Z" fill="url(#flagWash)" opacity="0.9"/>
  </svg>

  <svg class="product-photo" viewBox="0 0 310 317" role="img" aria-label="White candle jar beside its tall black gift tube, with a small round lid in front">
    <defs>
      <linearGradient id="productTone" x1="0" y1="0" x2="1" y2="0">
        <stop offset="0" stop-color="var(--product-dark)"/>
        <stop offset="0.4" stop-color="#3a3a3a"/>
        <stop offset="0.55" stop-color="var(--product-light)"/>
        <stop offset="1" stop-color="#d8d8d8"/>
      </linearGradient>
    </defs>
    <rect x="0" y="0" width="310" height="317" rx="12" fill="url(#productTone)"/>
  </svg>

  <h1 class="headline">MEMORIAL DAY SALE</h1>
  <p class="fine-print">*with a minimum order of $50.00</p>

  <div class="offer-band">
    <p class="offer-text"><span class="percent">25%</span> OFF select candles &amp; FREE SHIPPING*</p>
  </div>
</main>
</body>
</html>
```